Supplement Rebranding Bottle Design

READ WORD DOCUMENT ATTACHED.
We want to rebrand our current health supplements (see below). We do want it to be modern, vibrant and appealing. Very upscale and elegant as it targets primarily women.
Bottle size: see pictures for bottle size, along with sample bottles that we like; we’re open to any bottle similar to the ones attached.
Current bottles: So ideally, we’d keep the core color on each bottle with a new branding/bottle design. But we're open to your suggestion.

Target Market(s)

mostly women but shouldn't be overly feminine

Requirements
Must have
• see bottle sizes attached

```html
<!DOCTYPE html>
<html lang="en">
<head>
<meta charset="utf-8">
<title>Supplement Label Series</title>
<link rel="stylesheet" href="https://fonts.googleapis.com/css2?family=Italiana&family=Marcellus&family=Cormorant+Garamond:wght@500&display=swap">
<style>
  :root {
    --backdrop: #e6e6e6;
    --label: #fdfdfd;
    --ink: #1b1b1b;
    --green-light: #5ddf8c;
    --green-dark: #3aa856;
    --purple-light: #9a78c8;
    --purple-dark: #5a2a84;
    --red-light: #e5374c;
    --red-dark: #b8172b;
    --pill-text: #ffffff;
  }
  * { box-sizing: border-box; margin: 0; padding: 0; }
  html, body {
    width: 1200px;
    height: 960px;
    overflow: hidden;
    background: var(--backdrop);
  }
  .label-series {
    width: 1200px;
    height: 960px;
    display: flex;
    align-items: center;
    justify-content: center;
    gap: 40px;
  }
  .label {
    width: 340px;
    height: 460px;
    background: var(--label);
    border-radius: 24px;
    display: flex;
    align-items: center;
    padding: 0 26px 0 34px;
    gap: 20px;
  }
  .label__band {
    flex: 0 0 58px;
    height: 360px;
    border-radius: 8px 8px 29px 29px;
    display: flex;
    align-items: center;
    justify-content: center;
  }
  .label--hormone .label__band { background: linear-gradient(180deg, var(--green-light), var(--green-dark)); }
  .label--liver .label__band { background: linear-gradient(180deg, var(--purple-light), var(--purple-dark)); }
  .label--tummy .label__band { background: linear-gradient(180deg, var(--red-light), var(--red-dark)); }
  .label__product-name {
    writing-mode: vertical-rl;
    transform: rotate(180deg);
    font-family: "Italiana", serif;
    font-size: 42px;
    color: var(--pill-text);
    white-space: nowrap;
    letter-spacing: 0.5px;
  }
  .label__info {
    flex: 1;
    text-align: center;
    color: var(--ink);
  }
  .label__claim {
    font-family: "Marcellus", serif;
    font-size: 27px;
    line-height: 1.22;
    font-weight: 400;
  }
  .label__type {
    font-family: "Cormorant Garamond", serif;
    font-weight: 500;
    font-size: 18px;
    margin-top: 10px;
  }
  .label__count {
    display: inline-block;
    margin-top: 16px;
    min-width: 68px;
    padding: 3px 14px;
    border-radius: 14px;
    font-family: "Cormorant Garamond", serif;
    font-size: 16px;
    color: var(--pill-text);
  }
  .label--hormone .label__count { background: linear-gradient(90deg, var(--green-dark), var(--green-light)); }
  .label--liver .label__count { background: linear-gradient(90deg, var(--purple-dark), var(--purple-light)); }
  .label--tummy .label__count { background: linear-gradient(90deg, var(--red-dark), var(--red-light)); }
  .label__form {
    font-family: "Cormorant Garamond", serif;
    font-weight: 500;
    font-size: 17px;
    margin-top: 14px;
  }
</style>
</head>
<body>
  <main class="label-series">
    <section class="label label--hormone">
      <div class="label__band"><span class="label__product-name">Hormone Bloom</span></div>
      <div class="label__info">
        <h2 class="label__claim">Supports<br>Healthy<br>Hormone<br>Levels</h2>
        <p class="label__type">Dietary Supplement</p>
        <span class="label__count">60</span>
        <p class="label__form">Vegetable Capsules</p>
      </div>
    </section>

    <section class="label label--liver">
      <div class="label__band"><span class="label__product-name">Liver Bloom</span></div>
      <div class="label__info">
        <h2 class="label__claim">Rejuvenating<br>Cleanse &amp;<br>Detox<br>Formula</h2>
        <p class="label__type">Dietary Supplement</p>
        <span class="label__count">120</span>
        <p class="label__form">Vegetable Capsules</p>
      </div>
    </section>

    <section class="label label--tummy">
      <div class="label__band"><span class="label__product-name">Tummy Bloom</span></div>
      <div class="label__info">
        <h2 class="label__claim">Oxygenating<br>Colon<br>Cleanse</h2>
        <p class="label__type">Dietary Supplement</p>
        <span class="label__count">90</span>
        <p class="label__form">Vegetable Capsules</p>
      </div>
    </section>
  </main>
</body>
</html>
```